Business card for someone who trains leaders
Organizational Development Consultant Business Card - Consulting
Organizational Development Consultant Business Card
Bright & Fun-filled
Darla Quinby
Capacity Development Adviser
(NO ADDRESS IS LISTED ON CARD)
darla@vrmthrivewell.com
www.netprofile/in/marlowquinby
I want a business card that says professional but not too corporate. I want it to only use the colors on my logo (plus white of course). I like the look of cards that have some black backgrounds, but I'm open to a lot of different looks - as long as it meshes well with the look and feel of the business card. I don't want anything too busy, but yet want something that stands out a bit.
Where Will Your Growth Lead? Let VRM Thrivewell help you find growth through organizational development, leadership coaching, and much more!
marlowquinby marlowquinby
Please don't submit generic samples with someone else's information. I'm only interested in seeing completed business cards with the information I included in the creative brief.
I would like to see some designs that are on a white background as well as a black background. I'm not sold either way, but want to see a variety. Also, on the creative brief, I left off the website. In addition to my netprofile profile, I also want the website www.vrmthrivewell.com.

```html
<!DOCTYPE html>
<html lang="en">
<head>
<meta charset="utf-8">
<title>VRM Thrivewell – Business Card</title>
<link href="https://fonts.googleapis.com/css2?family=Open+Sans:wght@400;600;700&display=swap" rel="stylesheet">
<style>
  :root {
    --purple: #6a2c91;
    --purple-light: #8a4cb3;
    --blue: #1f8fd0;
    --grey: #8e8f94;
    --grey-light: #c9cacd;
    --ink: #333338;
    --white: #ffffff;
    --backdrop: #e6e6e9;
  }
  * { box-sizing: border-box; margin: 0; padding: 0; }
  html, body { width: 1200px; height: 908px; overflow: hidden; }
  body {
    background: var(--backdrop);
    font-family: "Open Sans", Arial, sans-serif;
    color: var(--ink);
    position: relative;
  }
  .card {
    position: absolute;
    top: 305px;
    width: 530px;
    height: 303px;
    border-radius: 18px;
    background: var(--white);
    overflow: hidden;
    box-shadow: 0 6px 18px rgba(0,0,0,.18);
  }
  .card--front { left: 50px; }
  .card--back { left: 620px; }

  /* front */
  .front-emblem {
    position: absolute;
    right: 36px; top: 26px;
    width: 210px; height: 210px;
    border-radius: 50%;
    background: radial-gradient(circle at 35% 30%, var(--purple-light), var(--purple) 60%, #4d1d6c);
  }
  .brand {
    position: absolute;
    left: 30px;
    font-weight: 700;
    color: var(--purple);
    letter-spacing: .5px;
    white-space: nowrap;
  }
  .front-brand { top: 116px; font-size: 24px; }
  .tagline {
    position: absolute;
    font-size: 10.5px;
    color: var(--grey);
    font-style: italic;
    white-space: nowrap;
  }
  .front-tagline { left: 30px; top: 148px; padding-top: 3px; border-top: 1px solid var(--grey-light); width: 200px; }
  .front-pitch {
    position: absolute;
    left: 30px; top: 180px;
    width: 250px;
    font-size: 12px;
    font-weight: 600;
    line-height: 1.35;
    color: var(--ink);
  }

  /* back */
  .back-bands { position: absolute; inset: 0; }
  .back-mark {
    position: absolute;
    left: 72px; top: 180px;
    width: 36px; height: 36px;
    border-radius: 50%;
    background: var(--purple);
  }
  .back-brand { left: 116px; top: 183px; font-size: 20px; }
  .back-tagline { left: 116px; top: 212px; }
  .contact {
    position: absolute;
    left: 330px; top: 52px;
    color: var(--white);
  }
  .contact-name { font-size: 17px; font-weight: 600; }
  .contact-title { font-size: 11px; margin-bottom: 14px; }
  .contact-list { list-style: none; font-size: 10.5px; line-height: 1.75; }
  .contact-list li { display: flex; align-items: center; gap: 7px; }
  .contact-list svg { width: 10px; height: 10px; flex: none; }
</style>
</head>
<body>
  <section class="card card--front" aria-label="Card front">
    <div class="front-emblem"></div>
    <div class="brand front-brand">VRM THRIVEWELL</div>
    <div class="tagline front-tagline">Where Will Your Growth Lead?</div>
    <p class="front-pitch">Let VRM Thrivewell help you find growth through organizational development, leadership coaching, and much more!</p>
  </section>

  <section class="card card--back" aria-label="Card back">
    <svg class="back-bands" viewBox="0 0 530 303" preserveAspectRatio="none">
      <path d="M0 150 C60 128 150 118 220 132 C320 152 360 303 470 303 L530 303 L530 0 L0 0 Z" fill="#8e8f94"/>
      <path d="M0 138 C60 118 150 108 225 122 C325 142 365 290 480 296 L530 296 L530 0 L0 0 Z" fill="#1f8fd0"/>
      <path d="M0 128 C60 108 150 98 230 112 C330 132 375 280 490 288 L530 288 L530 0 L0 0 Z" fill="#6a2c91"/>
    </svg>
    <div class="back-mark"></div>
    <div class="brand back-brand">VRM THRIVEWELL</div>
    <div class="tagline back-tagline">Where Will Your Growth Lead?</div>
    <div class="contact">
      <div class="contact-name">Darla Quinby</div>
      <div class="contact-title">Capacity Development Adviser</div>
      <ul class="contact-list">
        <li><svg viewBox="0 0 10 10"><path d="M2 1 L4 1 L4.6 3 L3.5 3.8 C4 5 5 6 6.2 6.5 L7 5.4 L9 6 L9 8 C5 9 1 5 2 1 Z" fill="#fff"/></svg>435-555-0147</li>
        <li><svg viewBox="0 0 10 10"><rect x="1" y="2.5" width="8" height="5.5" fill="none" stroke="#fff"/><path d="M1 2.5 L5 5.5 L9 2.5" fill="none" stroke="#fff"/></svg>darla@vrmthrivewell.com</li>
        <li><svg viewBox="0 0 10 10"><rect x="1" y="1" width="8" height="8" rx="1.5" fill="#fff"/></svg>www.netprofile/in/marlowquinby</li>
        <li><svg viewBox="0 0 10 10"><circle cx="5" cy="5" r="4" fill="none" stroke="#fff"/><path d="M1 5 H9 M5 1 C3 3 3 7 5 9 M5 1 C7 3 7 7 5 9" fill="none" stroke="#fff" stroke-width=".7"/></svg>www.vrmthrivewell.com</li>
      </ul>
    </div>
  </section>
</body>
</html>
```